kestrelnet9 - a safety solution for schools

A Amok App for schools needs your help to design some screens. Its important to have a very simple use of the app. The function of the app is very easy, you put the button to trigger the alarm. The app has a message function. So we need 3 howto screens. you find a better description of the project in the briefing-file. If you have any questions just ask. Thanks in advance for the suggestions. Best Regards, Lars

Target Market(s)

Schools

Industry/Entity Type

Security Service

Font styles to use
Sans Serif

Colors

Designer to choose colors to be used in the design.

Requirements
Must have
• Simple, easy to use, look like a security app, trust,

```html
<!DOCTYPE html>
<html lang="de">
<head>
<meta charset="utf-8">
<title>kestrelnet9 – App Screens</title>
<link href="https://fonts.googleapis.com/css2?family=Roboto:wght@300;400;700&display=swap" rel="stylesheet">
<style>
  :root {
    --bg: #040306;
    --screen-top: #3c0204;
    --screen-bottom: #0b0103;
    --screen-edge: #0d0a12;
    --red: #d2171c;
    --red-bright: #ff2a2a;
    --red-deep: #8d0a0d;
    --ring: #2a0204;
    --hub: #140002;
    --icon: #a8080c;
    --icon-dot: #ff6a6a;
    --text: #ffffff;
    --text-soft: #e8d6d6;
    --rule: rgba(255,255,255,0.16);
  }
  * { margin: 0; padding: 0; box-sizing: border-box; }
  html, body { width: 1200px; height: 1200px; overflow: hidden; background: var(--bg); }
  .canvas {
    position: relative; width: 1200px; height: 1200px; overflow: hidden;
    font-family: "Roboto", Arial, sans-serif; color: var(--text);
    background:
      radial-gradient(ellipse 420px 360px at 260px 360px, rgba(110,0,6,0.45), transparent 70%),
      var(--bg);
  }
  .screen {
    position: absolute; overflow: hidden;
    background:
      radial-gradient(circle 90px at 30% 20%, rgba(150,0,10,0.35), transparent 70%),
      radial-gradient(circle 120px at 95% 55%, rgba(140,0,8,0.35), transparent 70%),
      linear-gradient(180deg, var(--screen-top) 0%, #220103 55%, var(--screen-bottom) 100%);
  }
  .screen::before {
    content: ""; position: absolute; left: 0; top: 0; bottom: 0; width: 17%;
    background: linear-gradient(180deg, rgba(30,0,2,0.4), var(--screen-edge));
  }
  .screen::after {
    content: ""; position: absolute; left: 17%; right: 0; top: 0; height: 24%;
    background: linear-gradient(180deg, rgba(40,0,3,0.6), transparent);
  }
  .screen > * { position: absolute; z-index: 1; }
  .rule { height: 1px; background: var(--rule); }

  /* login */
  .screen-login { left: 65px; top: 310px; width: 393px; height: 696px; }
  .brand-dot { left: 106px; top: 356px; width: 58px; height: 58px; border-radius: 50%; background: var(--red); }
  .screen-login .rule { left: 101px; top: 442px; width: 199px; }
  .brand-name { left: 101px; top: 460px; font-size: 32px; font-weight: 700; letter-spacing: 0.5px; }
  .tagline { left: 101px; top: 508px; font-size: 17px; font-weight: 300; color: var(--text-soft); letter-spacing: -0.3px; }
  .btn-login {
    left: 102px; top: 563px; width: 199px; height: 41px; background: linear-gradient(180deg, #c8161b, #a80f13);
    color: var(--text-soft); font-size: 19px; font-weight: 300; display: flex; align-items: center; justify-content: center;
  }

  /* registration */
  .screen-register { left: 500px; top: 36px; width: 311px; height: 549px; }
  .field { left: 81px; width: 155px; text-align: center; font-size: 14px; font-weight: 300; letter-spacing: -0.3px; }
  .forgot { left: 81px; width: 155px; top: 496px; text-align: center; font-size: 10px; font-weight: 300; letter-spacing: -0.2px; }

  .screen-title { left: 20px; right: 20px; text-align: center; font-weight: 700; font-size: 25px; line-height: 23px; }
  .screen-demo { left: 826px; top: 36px; width: 311px; height: 549px; }
  .demo-text { left: 40px; right: 20px; top: 152px; text-align: center; font-size: 14px; font-weight: 300; line-height: 18px; color: var(--text-soft); }
  .siren-area {
    left: 62px; top: 240px; width: 184px; height: 172px;
    background: radial-gradient(ellipse 95px 90px at 50% 50%, rgba(200,20,26,0.55), rgba(90,5,8,0.25) 70%, transparent 100%);
  }

  .screen-cancel { left: 500px; top: 616px; width: 311px; height: 549px; }
  .screen-office { left: 826px; top: 616px; width: 311px; height: 549px; }
  .dial { left: 62px; top: 250px; width: 200px; height: 200px; }
  .toolbar { top: 484px; left: 108px; display: flex; gap: 43px; align-items: center; }
  .toolbar svg { width: 30px; height: 30px; }
</style>
</head>
<body>
<div class="canvas">

  <section class="screen screen-login">
    <div class="brand-dot"></div>
    <div class="rule"></div>
    <div class="brand-name">KESTRELNET9</div>
    <div class="tagline">Weil Sicherheit Priorität hat!</div>
    <div class="btn-login">LOG IN</div>
  </section>

  <section class="screen screen-register">
    <div class="field" style="top:255px">VORNAME</div>
    <div class="rule" style="left:81px;top:288px;width:155px"></div>
    <div class="field" style="top:302px">NACHNAME</div>
    <div class="rule" style="left:81px;top:334px;width:155px"></div>
    <div class="field" style="top:348px">EMAIL ADRESS</div>
    <div class="rule" style="left:81px;top:380px;width:155px"></div>
    <div class="field" style="top:398px">SCHULE</div>
    <div class="rule" style="left:81px;top:428px;width:155px"></div>
    <div class="forgot">FORGET PASSWORD?</div>
  </section>

  <section class="screen screen-demo">
    <div class="screen-title" style="top:100px">DEMO MODUS</div>
    <div class="rule" style="left:91px;top:138px;width:155px"></div>
    <div class="demo-text">Teste den Alarm einmal, bevor<br>du im Notfall wirklich brauchst.</div>
    <div class="siren-area" role="img" aria-label="Illustration einer roten Alarm-Rundumleuchte"></div>
    <div class="toolbar">
      <svg viewBox="0 0 24 24" aria-hidden="true"><path fill="var(--icon)" d="M19.4 13a7.8 7.8 0 0 0 0-2l2.1-1.6-2-3.5-2.5 1a7.6 7.6 0 0 0-1.7-1L15 3h-4l-.4 2.9a7.6 7.6 0 0 0-1.7 1l-2.5-1-2 3.5L6.6 11a7.8 7.8 0 0 0 0 2l-2.1 1.6 2 3.5 2.5-1a7.6 7.6 0 0 0 1.7 1L11 21h4l.4-2.9a7.6 7.6 0 0 0 1.7-1l2.5 1 2-3.5zM13 15.5a3.5 3.5 0 1 1 0-7 3.5 3.5 0 0 1 0 7z" transform="translate(-1 0)"/></svg>
      <svg viewBox="0 0 24 24" aria-hidden="true"><path fill="var(--icon)" d="M2 3h20v14H9l-5 4v-4H2z"/><circle cx="8" cy="10" r="1.2" fill="var(--icon-dot)"/><circle cx="12" cy="10" r="1.2" fill="var(--icon-dot)"/><circle cx="16" cy="10" r="1.2" fill="var(--icon-dot)"/></svg>
    </div>
  </section>

  <section class="screen screen-cancel">
    <div class="screen-title" style="top:101px">ALARM<br>ABBRECHEN</div>
    <div class="rule" style="left:75px;top:162px;width:155px"></div>
    <svg class="dial" viewBox="0 0 200 200" aria-hidden="true">
      <circle cx="100" cy="100" r="92" fill="var(--ring)" stroke="#4a0306" stroke-width="2"/>
      <circle cx="100" cy="100" r="78" fill="none" stroke="var(--red-bright)" stroke-width="28" pathLength="500" opacity="0.9" transform="rotate(-100 100 100)" style="stroke-dasharray:3 2.5;"/>
      <circle cx="100" cy="100" r="78" fill="none" stroke="var(--ring)" stroke-width="30" pathLength="500" stroke-dasharray="361 139" stroke-dashoffset="-139" transform="rotate(-100 100 100)"/>
      <circle cx="100" cy="100" r="62" fill="var(--hub)"/>
      <circle cx="100" cy="100" r="46" fill="var(--red)"/>
      <text x="100" y="116" text-anchor="middle" font-family="Roboto, Arial, sans-serif" font-weight="700" font-size="48" fill="var(--red-deep)">4</text>
      <text x="100" y="137" text-anchor="middle" font-family="Roboto, Arial, sans-serif" font-size="11" fill="var(--red-deep)">Sec.</text>
      <path d="M178 105l-5-5a3 3 0 0 1 5-3 3 3 0 0 1 5 3z" fill="var(--red-deep)"/>
    </svg>
    <div class="toolbar">
      <svg viewBox="0 0 24 24" aria-hidden="true"><path fill="var(--icon)" d="M19.4 13a7.8 7.8 0 0 0 0-2l2.1-1.6-2-3.5-2.5 1a7.6 7.6 0 0 0-1.7-1L15 3h-4l-.4 2.9a7.6 7.6 0 0 0-1.7 1l-2.5-1-2 3.5L6.6 11a7.8 7.8 0 0 0 0 2l-2.1 1.6 2 3.5 2.5-1a7.6 7.6 0 0 0 1.7 1L11 21h4l.4-2.9a7.6 7.6 0 0 0 1.7-1l2.5 1 2-3.5zM13 15.5a3.5 3.5 0 1 1 0-7 3.5 3.5 0 0 1 0 7z" transform="translate(-1 0)"/></svg>
      <svg viewBox="0 0 24 24" aria-hidden="true"><path fill="var(--icon)" d="M2 3h20v14H9l-5 4v-4H2z"/><circle cx="8" cy="10" r="1.2" fill="var(--icon-dot)"/><circle cx="12" cy="10" r="1.2" fill="var(--icon-dot)"/><circle cx="16" cy="10" r="1.2" fill="var(--icon-dot)"/></svg>
    </div>
  </section>

  <section class="screen screen-office">
    <div class="screen-title" style="top:78px">Sekretariat:<br>Bitte bleiben Sie<br>wo Sie sind</div>
    <div class="rule" style="left:75px;top:162px;width:155px"></div>
    <svg class="dial" viewBox="0 0 200 200" aria-hidden="true">
      <circle cx="100" cy="100" r="92" fill="var(--ring)" stroke="#4a0306" stroke-width="2"/>
      <circle cx="100" cy="100" r="78" fill="none" stroke="var(--red-bright)" stroke-width="28" pathLength="500" opacity="0.9" transform="rotate(-100 100 100)" style="stroke-dasharray:3 2.5;"/>
      <circle cx="100" cy="100" r="78" fill="none" stroke="var(--ring)" stroke-width="30" pathLength="500" stroke-dasharray="361 139" stroke-dashoffset="-139" transform="rotate(-100 100 100)"/>
      <circle cx="100" cy="100" r="62" fill="var(--hub)"/>
      <circle cx="100" cy="100" r="46" fill="var(--red)"/>
      <text x="100" y="116" text-anchor="middle" font-family="Roboto, Arial, sans-serif" font-weight="700" font-size="48" fill="var(--red-deep)">4</text>
      <text x="100" y="137" text-anchor="middle" font-family="Roboto, Arial, sans-serif" font-size="11" fill="var(--red-deep)">Sec.</text>
      <path d="M178 105l-5-5a3 3 0 0 1 5-3 3 3 0 0 1 5 3z" fill="var(--red-deep)"/>
    </svg>
    <div class="toolbar">
      <svg viewBox="0 0 24 24" aria-hidden="true"><path fill="var(--icon)" d="M19.4 13a7.8 7.8 0 0 0 0-2l2.1-1.6-2-3.5-2.5 1a7.6 7.6 0 0 0-1.7-1L15 3h-4l-.4 2.9a7.6 7.6 0 0 0-1.7 1l-2.5-1-2 3.5L6.6 11a7.8 7.8 0 0 0 0 2l-2.1 1.6 2 3.5 2.5-1a7.6 7.6 0 0 0 1.7 1L11 21h4l.4-2.9a7.6 7.6 0 0 0 1.7-1l2.5 1 2-3.5zM13 15.5a3.5 3.5 0 1 1 0-7 3.5 3.5 0 0 1 0 7z" transform="translate(-1 0)"/></svg>
      <svg viewBox="0 0 24 24" aria-hidden="true"><path fill="var(--icon)" d="M2 3h20v14H9l-5 4v-4H2z"/><circle cx="8" cy="10" r="1.2" fill="var(--icon-dot)"/><circle cx="12" cy="10" r="1.2" fill="var(--icon-dot)"/><circle cx="16" cy="10" r="1.2" fill="var(--icon-dot)"/></svg>
    </div>
  </section>

</div>
</body>
</html>
```